Natural healthcare clinic needs stationery and business card design

We have had a logo developed by Pixel Harbor and are now looking at utilising it for a new business concept. The concept is a natural healthcare clinic that hosts a number of small businesses. The individual practitioners may want to utilise the host business stationery to provide a consistent message to clients.

I am looking for a stationery design - letterhead, DL brochure template and business card that uses our logo. The business name 'Bright Meadows' is all about getting rhythm back into your life so you can be fit and healthy. The stationery design should reflect this.

There are a couple of requirements for the business card, it needs to be double-sided with black and white back. There should be lines to write appointment times on. The cards may need to be custom named on the front for example Carys Dunmore, Remedial Therapist and Aromatherapist. Therefore if a template can be provided so we can customise this information using MS Publisher, it would be appreciated.

The DL brochure template needs to be A4 folded to DL. I am looking for a consistent brand message that can be utilised to produce our own clinic brochures.

The natural healthcare clinic will host the following types of businesses - remedial massage, pregnancy massage, oncology massage, aromatherapy, acupuncture - as a bit of a guide.

Target Market(s)

25-45 year old male and females who work full time.

Industry/Entity Type

Healthcare

Requirements
Must have
• Use the logo I have already.

```html
<!DOCTYPE html>
<html lang="en">
<head>
<meta charset="utf-8">
<title>Bright Meadows Stationery Set</title>
<link href="https://fonts.googleapis.com/css2?family=Open+Sans:wght@400;600;700&display=swap" rel="stylesheet">
<style>
  :root{
    --backdrop:#4b3124;
    --olive:#8a9a46;
    --olive-dark:#66752a;
    --leaf:#8cc63f;
    --leaf-light:#b5d96a;
    --title-red:#e2231a;
    --service-blue:#2e3192;
    --ink:#4a4a4a;
    --paper:#ffffff;
    --mist:#e9eaec;
    --skin:#e8b48c;
    --label:#ffffff;
  }
  *{box-sizing:border-box;margin:0;padding:0}
  html,body{width:1200px;height:675px;overflow:hidden}
  body{background:var(--backdrop);font-family:"Open Sans",Arial,sans-serif;position:relative;color:var(--ink)}
  .abs{position:absolute}
  .view-label{position:absolute;color:var(--label);font-weight:700;font-size:15px}
  .sheet{position:absolute;background:var(--paper);box-shadow:0 3px 8px rgba(0,0,0,.45);overflow:hidden}
  .brand-name{font-weight:600;color:var(--olive-dark);white-space:nowrap;line-height:1}
  .brand-tag{font-size:6px;color:var(--ink);font-weight:600}
  .dot{display:inline-block;border-radius:50%;background:var(--leaf);vertical-align:middle}
  .photo{position:absolute}
  .copy{font-size:4.6px;line-height:1.45;text-align:justify}
  .ribbon{position:absolute;height:13px;background:linear-gradient(90deg,var(--leaf),var(--olive));color:#fff;font-size:8px;font-weight:600;padding:1px 0 0 14px;clip-path:polygon(0 0,88% 0,100% 50%,88% 100%,0 100%)}
  .band-top{position:absolute;left:0;right:0;top:0;height:11px;background:linear-gradient(90deg,var(--leaf),var(--olive))}
  /* letterhead */
  .letterhead{left:58px;top:54px;width:360px;height:466px}
  .letterhead .footer-band{position:absolute;left:0;top:435px;width:245px;height:17px;background:linear-gradient(90deg,var(--leaf),var(--olive));clip-path:polygon(0 0,100% 0,94% 100%,0 100%)}
  .letterhead .footer-tail{position:absolute;left:236px;top:443px;width:124px;height:9px;background:var(--olive-dark)}
  .letterhead .footer-text{position:absolute;top:439px;font-size:4.5px;color:#eef5dc}
  /* brochure */
  .brochure{top:54px;width:351px;height:496px;display:flex}
  .brochure .panel{position:relative;width:50%;height:100%;overflow:hidden}
  .panel-olive{background:var(--olive);color:#fff}
  .panel-mist{background:linear-gradient(180deg,#f4f4f5,var(--mist))}
  .panel-heading{position:absolute;left:13px;font-size:12.5px;font-weight:600;line-height:1.35;color:#fff}
  .phone{font-weight:700;color:#fff}
  /* cards */
  .card{width:150px;height:86px;top:0}
  .card .strip{position:absolute;left:0;bottom:0;width:100%;height:13px;background:var(--olive-dark)}
  .card .strip-leaf{position:absolute;left:0;bottom:6px;width:100%;height:8px;background:linear-gradient(90deg,var(--leaf-light),var(--leaf));clip-path:polygon(0 0,100% 0,100% 100%,0 100%)}
  .card .appt-line{position:absolute;left:14px;right:12px;height:1px;background:var(--leaf)}
  .card .appt-label{position:absolute;right:10px;bottom:2px;font-size:7px;color:#fff;font-weight:600}
  .card .clinic-label{position:absolute;left:10px;bottom:3px;font-size:5px;color:#fff}
</style>
</head>
<body>

<div class="view-label" style="left:58px;top:24px">Letterhead option 5 (Dec 16)</div>
<div class="view-label" style="left:443px;top:28px">Back</div>
<div class="view-label" style="left:746px;top:26px">Front</div>
<div class="view-label" style="left:808px;top:27px">Front Inside</div>
<div class="view-label" style="left:1071px;top:32px">Back Inside</div>

<!-- Letterhead -->
<section class="sheet letterhead" aria-label="Letterhead">
  <div class="abs" style="left:22px;top:66px">
    <span class="dot" style="width:7px;height:7px"></span>
    <span class="brand-name" style="font-size:13px">Bright Meadows</span>
    <div class="brand-tag" style="margin:2px 0 0 11px">Well Being Clinic</div>
  </div>
  <div class="footer-band"></div>
  <div class="footer-tail"></div>
  <span class="footer-text" style="left:26px">012.345.6789</span>
  <span class="footer-text" style="left:76px">Suite 000, City name</span>
  <span class="footer-text" style="left:158px">www.brightmeadows.com</span>
</section>

<!-- Business cards, named set -->
<div class="abs" style="left:58px;top:548px">
  <section class="sheet card" style="left:0" aria-label="Business card front">
    <div class="abs" style="left:10px;top:24px">
      <span class="brand-name" style="font-size:9px">Bright Meadows</span>
      <div class="brand-tag" style="font-size:5px;margin-top:2px">Well Being Clinic</div>
    </div>
    <div class="abs" style="left:98px;top:8px;font-size:6px;color:var(--olive)">CARYS DUNMORE</div>
    <div class="abs" style="left:98px;top:16px;font-size:4px;color:var(--olive)">Remedial Therapist<br>Aromatherapist</div>
    <div class="strip"></div><div class="strip-leaf"></div>
    <span class="clinic-label" style="font-size:3.8px">012.345.6789 &nbsp; www.brightmeadows.com</span>
  </section>
  <section class="sheet card" style="left:159px" aria-label="Business card back">
    <div class="appt-line" style="top:16px"></div>
    <div class="appt-line" style="top:30px"></div>
    <div class="appt-line" style="top:44px"></div>
    <div class="appt-line" style="top:58px"></div>
    <div class="strip"></div><div class="strip-leaf"></div>
    <span class="clinic-label">Well Being Clinic</span>
    <span class="appt-label">Appointment</span>
  </section>
</div>

<!-- Brochure outside -->
<div class="sheet brochure" style="left:441px" aria-label="Brochure outside">
  <div class="panel panel-olive">
    <div class="photo" role="img" aria-label="Photo of a client relaxing during a massage" style="left:0;top:0;width:100%;height:106px;background:linear-gradient(135deg,#e9dcd0,#c98a6a 55%,#8b2a2a)"></div>
    <div class="abs" style="left:0;top:106px;width:100%;height:14px;background:linear-gradient(90deg,#c9c9c9,#f2f2f2)"></div>
    <div class="panel-heading" style="top:130px">Lorem Ipsum Dolor sit<br>Consectetur adipisicing</div>
    <div class="ribbon" style="left:0;top:182px;width:125px">Remedial Massage</div>
    <p class="copy abs" style="left:13px;top:200px;width:160px">Lorem ipsum dolor sit amet, consectetur adipisicing elit, sed do eiusmod tempor incididunt ut labore et dolore magna aliqua. Ut enim ad minim veniam, quis nostrud exercitation ullamco laboris nisi ut aliquip ex ea commodo consequat. Duis aute irure dolor in reprehenderit in voluptate velit esse cillum dolore eu fugiat nulla pariatur.</p>
    <div class="ribbon" style="left:0;top:259px;width:125px">Pregnancy Massage</div>
    <p class="copy abs" style="left:13px;top:277px;width:160px">Lorem ipsum dolor sit amet, consectetur adipisicing elit, sed do eiusmod tempor incididunt ut labore et dolore magna aliqua. Ut enim ad minim veniam, quis nostrud exercitation ullamco laboris nisi ut aliquip ex ea commodo consequat. Duis aute irure dolor in reprehenderit in voluptate velit esse cillum dolore eu fugiat nulla pariatur. Excepteur sint occaecat cupidatat non proident.</p>
    <div class="ribbon" style="left:0;top:334px;width:125px">Oncology Massage</div>
    <p class="copy abs" style="left:13px;top:352px;width:160px">Lorem ipsum dolor sit amet, consectetur adipisicing elit, sed do eiusmod tempor incididunt ut labore et dolore magna aliqua. Ut enim ad minim veniam, quis nostrud exercitation ullamco laboris nisi ut aliquip ex ea commodo consequat. Duis aute irure dolor in reprehenderit in voluptate velit esse cillum dolore eu fugiat nulla pariatur. Excepteur sint occaecat cupidatat non proident, sunt in culpa qui officia deserunt mollit anim id est laborum.</p>
    <div class="phone abs" style="left:13px;top:414px;font-size:15px">012.345.6789</div>
    <div class="abs" style="left:0;top:440px;width:100%;height:56px;background:var(--paper)"></div>
    <div class="abs" style="left:0;top:436px;width:100px;height:60px;background:linear-gradient(180deg,#f5f5f5,#d9d9d9);clip-path:polygon(0 0,100% 0,80% 100%,0 100%)"></div>
    <div class="abs" style="left:12px;top:463px">
      <span class="brand-name" style="font-size:8px">Bright Meadows</span>
      <div class="brand-tag" style="font-size:4.5px;margin-top:2px">Well Being Clinic</div>
    </div>
    <div class="abs" style="left:118px;top:454px;font-size:4.6px;line-height:1.5;color:var(--ink)">Suite 000, City name<br>Country name 00000<br><br>info@brightmeadows.com<br>www.brightmeadows.com</div>
  </div>
  <div class="panel panel-mist">
    <div class="band-top"></div>
    <div class="abs" style="left:0;width:100%;top:18px;text-align:center;color:var(--title-red);font-size:14px;font-weight:600;line-height:1.2">Lorem<br>Ipsum Dolor sit</div>
    <div class="abs" style="left:0;width:100%;top:58px;text-align:center;color:var(--service-blue);font-size:8.5px;font-weight:600;line-height:1.35">Remedial Massage<br>Pregnancy Massage, Oncology<br>Massage, Aromatherapy,<br>Acupuncture</div>
    <div class="abs" style="left:14px;top:180px">
      <span class="dot" style="width:8px;height:8px"></span>
      <span class="brand-name" style="font-size:13px">Bright Meadows</span>
      <div class="brand-tag" style="margin:5px 0 0 2px">Well Being Clinic</div>
    </div>
    <p class="copy abs" style="left:13px;top:240px;width:152px">Lorem ipsum dolor sit amet, consectetur adipisicing elit, sed do eiusmod tempor incididunt ut labore et dolore magna aliqua. Ut enim ad minim veniam, quis nostrud exercitation ullamco laboris nisi.</p>
    <div class="photo" role="img" aria-label="Photo of hands massaging a back" style="left:13px;top:283px;width:157px;height:90px;border-radius:5px;background:linear-gradient(135deg,#f7d2ad,#e4a06b 60%,#c77b45);box-shadow:0 1px 3px rgba(0,0,0,.3)"></div>
    <div class="photo" role="img" aria-label="Photo of a massage treatment" style="left:13px;top:383px;width:157px;height:90px;border-radius:5px;background:linear-gradient(135deg,#e9c6a8,#b07c5a 55%,#f0e3d8);box-shadow:0 1px 3px rgba(0,0,0,.3)"></div>
    <div class="abs" style="left:0;top:480px;width:100%;height:16px;background:var(--olive-dark)"></div>
    <div class="abs" style="left:0;top:480px;width:80%;height:10px;background:linear-gradient(90deg,var(--leaf),var(--olive));clip-path:polygon(0 0,100% 0,94% 100%,0 100%)"></div>
    <div class="phone abs" style="left:12px;top:478px;font-size:11px">012.345.6789</div>
    <div class="abs" style="left:12px;top:489px;font-size:5.5px;color:#fff;font-weight:600;letter-spacing:.8px">www.brightmeadows.com</div>
  </div>
</div>

<!-- Business cards, generic set -->
<div class="abs" style="left:443px;top:567px">
  <section class="sheet card" style="left:0" aria-label="Business card front">
    <div class="abs" style="left:12px;top:36px">
      <span class="brand-name" style="font-size:9px">Bright Meadows</span>
    </div>
    <div class="strip"></div><div class="strip-leaf"></div>
  </section>
  <section class="sheet card" style="left:160px" aria-label="Business card back">
    <div class="appt-line" style="top:16px"></div>
    <div class="appt-line" style="top:30px"></div>
    <div class="appt-line" style="top:44px"></div>
    <div class="appt-line" style="top:58px"></div>
    <div class="strip"></div><div class="strip-leaf"></div>
    <span class="clinic-label">Well Being Clinic</span>
    <span class="appt-label">Appointment</span>
  </section>
</div>

<!-- Brochure inside -->
<div class="sheet brochure" style="left:806px" aria-label="Brochure inside">
  <div class="panel panel-mist">
    <div class="band-top"></div>
    <div class="photo" role="img" aria-label="Photo of a relaxed spa client" style="left:0;top:11px;width:100%;height:150px;background:linear-gradient(120deg,#f1e6dd,#d9b49a 45%,#3a2a24 80%,#f4f4f4)"></div>
    <div class="photo" role="img" aria-label="Photo of lavender salts and spa stones" style="left:12px;top:158px;width:115px;height:62px;border-radius:40% 50% 45% 40%;background:linear-gradient(135deg,#c9b2d8,#8e6aa8 50%,#3a3a3a)"></div>
    <div class="abs" style="left:20px;top:270px">
      <span class="dot" style="width:8px;height:8px"></span>
      <span class="brand-name" style="font-size:13px">Bright Meadows</span>
      <div class="brand-tag" style="margin:5px 0 0 2px">Well Being Clinic</div>
    </div>
    <div class="abs" style="left:0;width:100%;top:346px;text-align:center;font-size:12px;color:var(--olive-dark);font-weight:600">BRAND MESSAGE</div>
    <p class="copy abs" style="left:13px;top:372px;width:152px">Lorem ipsum dolor sit amet, consectetur adipisicing elit, sed do eiusmod tempor incididunt ut labore et dolore magna aliqua. Ut enim ad minim veniam, quis nostrud exercitation ullamco laboris nisi ut aliquip ex ea commodo consequat. Duis aute irure dolor in reprehenderit in voluptate velit esse cillum dolore eu fugiat nulla pariatur. Lorem ipsum dolor sit amet, consectetur adipisicing elit, sed do eiusmod tempor incididunt ut labore et dolore magna aliqua. Ut enim ad minim veniam, quis nostrud exercitation ullamco laboris nisi ut aliquip ex ea commodo consequat. Duis aute irure dolor in reprehenderit in voluptate velit esse cillum dolore eu fugiat nulla pariatur.</p>
    <p class="copy abs" style="left:13px;top:462px;width:152px">Lorem ipsum dolor sit amet, consectetur adipisicing elit, sed do eiusmod tempor incididunt ut labore et dolore magna aliqua. Ut enim ad minim veniam, quis nostrud exercitation ullamco laboris nisi ut aliquip ex ea commodo consequat.</p>
  </div>
  <div class="panel panel-olive">
    <div class="band-top"></div>
    <div class="panel-heading" style="top:28px">Lorem Ipsum Dolor sit<br>Consectetur adipisicing</div>
    <div class="photo" role="img" aria-label="Photo of a hot stone massage" style="left:11px;top:74px;width:155px;height:87px;border-radius:5px;background:linear-gradient(135deg,#e7b993,#c9744a 55%,#7a1e1e)"></div>
    <p class="copy abs" style="left:11px;top:173px;width:155px">Lorem ipsum dolor sit amet, consectetur adipisicing elit, sed do eiusmod tempor incididunt ut labore et dolore magna aliqua. Ut enim ad minim veniam, quis nostrud exercitation ullamco laboris nisi.</p>
    <div class="ribbon" style="left:0;top:221px;width:125px">Aromatherapy</div>
    <p class="copy abs" style="left:11px;top:239px;width:155px">Lorem ipsum dolor sit amet, consectetur adipisicing elit, sed do eiusmod tempor incididunt ut labore et dolore magna aliqua. Ut enim ad minim veniam, quis nostrud exercitation ullamco laboris nisi ut aliquip ex ea commodo consequat. Duis aute irure dolor in reprehenderit in voluptate velit esse cillum dolore eu fugiat nulla pariatur. Excepteur sint occaecat cupidatat non proident.</p>
    <div class="ribbon" style="left:0;top:294px;width:125px">Acupuncture</div>
    <p class="copy abs" style="left:11px;top:312px;width:155px">Lorem ipsum dolor sit amet, consectetur adipisicing elit, sed do eiusmod tempor incididunt ut labore et dolore magna aliqua. Ut enim ad minim veniam, quis nostrud exercitation ullamco laboris nisi ut aliquip ex ea commodo consequat. Duis aute irure dolor in reprehenderit in voluptate velit esse cillum dolore eu fugiat nulla pariatur.</p>
    <div class="photo" role="img" aria-label="Photo of an acupuncture treatment" style="left:11px;top:366px;width:155px;height:87px;border-radius:5px;background:linear-gradient(135deg,#dfe6ec,#e9c7a8 55%,#f6f6f6)"></div>
    <div class="abs" style="left:0;width:100%;top:460px;text-align:center;font-size:6px">For more information</div>
    <div class="phone abs" style="left:0;width:100%;top:467px;text-align:center;font-size:14px">012.345.6789</div>
    <div class="abs" style="left:0;width:100%;top:486px;text-align:center;font-size:6px;font-weight:600;letter-spacing:.8px">www.brightmeadows.com</div>
  </div>
</div>

</body>
</html>
```